Business card for massage therapy company called Brook Fern Wellness

Need business card for massage therapy company called Brook Fern Wellness. Would like my logo on the front and the back of the card I have 3 options of logos and you can play with what looks better.

Would like this information displayed on the back of the card:

Marcus Ellery
Licensed Massage Therapist
321-555-0147
brookfern-example.com
brookfern_rest_

```html
<!DOCTYPE html>
<html lang="en">
<head>
<meta charset="utf-8">
<title>Brook Fern Wellness – Business Card</title>
<link href="https://fonts.googleapis.com/css2?family=Montserrat:wght@300;400;600;700&display=swap" rel="stylesheet">
<style>
  :root {
    --backdrop: #1f1f22;
    --card: #ffffff;
    --olive: #747a60;
    --olive-light: #a3a592;
    --tan: #c49a78;
    --ink: #222222;
    --rule: #9a9a90;
  }
  * { box-sizing: border-box; margin: 0; padding: 0; }
  html, body {
    width: 1200px; height: 947px; overflow: hidden;
    background: var(--backdrop);
    font-family: "Montserrat", sans-serif;
  }
  .canvas {
    width: 1200px; height: 947px;
    display: flex; flex-direction: column; align-items: center; justify-content: center;
    gap: 27px;
  }
  .card {
    position: relative;
    width: 720px; height: 410px;
    background: var(--card);
    border-radius: 18px;
    overflow: hidden;
  }
  .card__wave { position: absolute; inset: 0; width: 100%; height: 100%; }

  /* Front */
  .front__brand {
    position: absolute; left: 70px; top: 110px;
    color: var(--olive);
    font-weight: 400;
    text-align: center;
    line-height: 1.1;
  }
  .front__brand-name { font-size: 54px; letter-spacing: 1px; }
  .front__brand-sub { font-size: 22px; letter-spacing: 12px; margin-top: 10px; }

  /* Back */
  .back__brand {
    position: absolute; left: 40px; top: 95px; width: 280px;
    display: flex; flex-direction: column; align-items: center;
    color: var(--olive); font-weight: 400;
    text-align: center;
  }
  .back__mark {
    width: 92px; height: 92px; border-radius: 50%;
    border: 2px solid var(--olive);
    margin-bottom: 20px;
  }
  .back__brand-name { font-size: 32px; letter-spacing: 3px; line-height: 1.1; }
  .back__brand-sub { font-size: 16px; letter-spacing: 9px; margin-top: 6px; }
  .back__divider {
    position: absolute; left: 345px; top: 70px;
    width: 1px; height: 215px; background: var(--rule);
  }
  .back__details { position: absolute; left: 380px; top: 62px; color: var(--ink); }
  .back__name { font-size: 27px; font-weight: 700; color: var(--olive); letter-spacing: 0.5px; }
  .back__title { font-size: 16px; color: var(--tan); margin-top: 2px; }
  .back__address { font-size: 15px; line-height: 1.45; margin-top: 22px; }
  .back__contacts { list-style: none; margin-top: 16px; font-size: 15px; line-height: 1.6; }
  .back__contacts li { display: flex; align-items: center; gap: 10px; }
  .back__contacts svg { width: 13px; height: 13px; fill: var(--tan); flex: none; }
</style>
</head>
<body>
<main class="canvas">

  <section class="card card--front" aria-label="Card front">
    <svg class="card__wave" viewBox="0 0 720 410" preserveAspectRatio="none" aria-hidden="true">
      <defs>
        <linearGradient id="front-shade" x1="0" y1="1" x2="1" y2="0">
          <stop offset="0" stop-color="#ffffff"/>
          <stop offset="1" stop-color="var(--olive-light)"/>
        </linearGradient>
      </defs>
      <path d="M300 410 C330 330 380 300 470 260 C580 210 620 120 720 70 L720 410 Z" fill="url(#front-shade)"/>
      <path d="M230 410 C270 330 330 300 430 280 C560 250 610 140 720 90 L720 410 Z" fill="var(--olive)"/>
    </svg>
    <div class="front__brand">
      <div class="front__brand-name">Brook Fern</div>
      <div class="front__brand-sub">WELLNESS</div>
    </div>
  </section>

  <section class="card card--back" aria-label="Card back">
    <svg class="card__wave" viewBox="0 0 720 410" preserveAspectRatio="none" aria-hidden="true">
      <path d="M470 410 C540 330 620 270 720 215 L720 410 Z" fill="var(--tan)"/>
      <path d="M490 410 C560 335 635 280 720 232 L720 410 Z" fill="#ffffff"/>
      <path d="M505 410 C575 340 645 290 720 250 L720 410 Z" fill="var(--olive)"/>
    </svg>

    <div class="back__brand">
      <div class="back__mark" aria-hidden="true"></div>
      <div class="back__brand-name">BROOK FERN</div>
      <div class="back__brand-sub">WELLNESS</div>
    </div>

    <div class="back__divider"></div>

    <div class="back__details">
      <h1 class="back__name">MARCUS ELLERY</h1>
      <p class="back__title">Licensed Massage Therapist</p>
      <p class="back__address">48 Alder Lane,<br>Millbrook, MA 02090</p>
      <ul class="back__contacts">
        <li>
          <svg viewBox="0 0 24 24" aria-hidden="true"><path d="M6.6 10.8a15.1 15.1 0 0 0 6.6 6.6l2.2-2.2c.3-.3.7-.4 1-.2 1.1.4 2.3.6 3.6.6.6 0 1 .4 1 1V20c0 .6-.4 1-1 1A17 17 0 0 1 3 4c0-.6.4-1 1-1h3.5c.6 0 1 .4 1 1 0 1.3.2 2.5.6 3.6.1.3 0 .7-.2 1z"/></svg>
          <span>321-555-0147</span>
        </li>
        <li>
          <svg viewBox="0 0 24 24" aria-hidden="true"><path d="M2 5h20v14H2z M4 7v.5l8 5 8-5V7l-8 5z" fill-rule="evenodd"/></svg>
          <span>info@brookfern-example.com</span>
        </li>
        <li>
          <svg viewBox="0 0 24 24" aria-hidden="true"><path d="M12 2a10 10 0 1 0 0 20 10 10 0 0 0 0-20zm0 2c.9 0 2.2 2 2.7 5H9.3C9.8 6 11.1 4 12 4zM4.3 11h3c0 .7 0 1.3.1 2h-3a8 8 0 0 1-.1-2zm5 0h5.4a17 17 0 0 1 0 2H9.3a17 17 0 0 1 0-2zm7.4 0h3a8 8 0 0 1-.1 2h-3l.1-2zM9.3 15h5.4c-.5 3-1.8 5-2.7 5s-2.2-2-2.7-5z"/></svg>
          <span>brookfern-example.com</span>
        </li>
      </ul>
    </div>
  </section>

</main>
</body>
</html>
```